Business Card for a Renewable energy construction company

I need a formal, neat looking business card. Minimal and professional looking. Back side can have a design that is semi-ransparent/shaded

Target Market(s)

Renewable energy companies

Contact Information for Business Card

Name, Surname and contact details (phone, email)

Colors
00AB8E
00BBA5
67D7C9
C6EFE9
E9F9F6

Requirements
Must have
• Place for a QR code in the back side

```html
<!DOCTYPE html>
<html lang="en">
<head>
<meta charset="utf-8">
<title>Halvern Business Card</title>
<link rel="stylesheet" href="https://fonts.googleapis.com/css2?family=Montserrat:ital,wght@0,400;0,700;1,300&display=swap">
<style>
  :root {
    --backdrop: #237f82;
    --card: #ffffff;
    --teal: #1e7f82;
    --ink: #231f20;
    --grey: #6d6e71;
    --shade-strong: #c9e4e5;
    --shade-soft: #e2f0f0;
  }
  * { margin: 0; padding: 0; box-sizing: border-box; }
  html, body {
    width: 1200px;
    height: 1200px;
    overflow: hidden;
    background: var(--backdrop);
    font-family: "Montserrat", Arial, sans-serif;
  }
  .card {
    position: absolute;
    left: 146px;
    width: 909px;
    height: 520px;
    background: var(--card);
    border-radius: 38px;
    overflow: hidden;
  }
  .card--front { top: 57px; }
  .card--back { top: 626px; left: 152px; }

  .back-shade {
    position: absolute;
    left: 0;
    top: 0;
    width: 540px;
    height: 100%;
    background: linear-gradient(115deg, var(--shade-soft) 0%, var(--shade-strong) 45%, var(--shade-soft) 80%, rgba(255,255,255,0) 100%);
    opacity: 0.85;
  }

  .brand {
    position: absolute;
    display: flex;
    align-items: center;
    gap: 10px;
    color: var(--ink);
    font-weight: 700;
    letter-spacing: 0.02em;
    line-height: 1;
  }
  .brand__dot {
    border-radius: 50%;
    background: var(--teal);
    flex: none;
  }
  .card--front .brand { left: 121px; top: 270px; font-size: 34px; }
  .card--front .brand__dot { width: 18px; height: 18px; }
  .card--back .brand { left: 555px; top: 262px; font-size: 50px; gap: 14px; }
  .card--back .brand__dot { width: 26px; height: 26px; }

  .person {
    position: absolute;
    left: 497px;
    top: 168px;
  }
  .person__name {
    color: var(--teal);
    font-weight: 700;
    font-size: 37px;
    line-height: 1;
  }
  .person__role {
    color: var(--grey);
    font-style: italic;
    font-weight: 300;
    font-size: 21px;
    margin-top: 8px;
    line-height: 1;
  }
  .person__rule {
    width: 56px;
    height: 2px;
    background: var(--teal);
    margin-top: 19px;
  }
  .contact {
    position: absolute;
    left: 497px;
    top: 280px;
    list-style: none;
  }
  .contact__item {
    display: flex;
    align-items: center;
    height: 30px;
    margin-bottom: 7px;
    color: var(--grey);
    font-size: 20px;
  }
  .contact__icon {
    width: 22px;
    height: 22px;
    margin-right: 36px;
    flex: none;
  }
</style>
</head>
<body>
  <section class="card card--front">
    <div class="brand"><span class="brand__dot"></span>Halvern</div>

    <div class="person">
      <h1 class="person__name">Mr. John Duo</h1>
      <p class="person__role">CEO</p>
      <div class="person__rule"></div>
    </div>

    <ul class="contact">
      <li class="contact__item">
        <svg class="contact__icon" viewBox="0 0 24 24" aria-hidden="true">
          <path fill="#1e7f82" d="M6.6 10.8a15.1 15.1 0 0 0 6.6 6.6l2.2-2.2a1 1 0 0 1 1-.25 11.4 11.4 0 0 0 3.6.57 1 1 0 0 1 1 1V20a1 1 0 0 1-1 1A17 17 0 0 1 3 4a1 1 0 0 1 1-1h3.5a1 1 0 0 1 1 1c0 1.25.2 2.45.57 3.57a1 1 0 0 1-.25 1z"/>
        </svg>
        (000) 000-1234
      </li>
      <li class="contact__item">
        <svg class="contact__icon" viewBox="0 0 24 24" aria-hidden="true">
          <circle cx="12" cy="12" r="4" fill="none" stroke="#1e7f82" stroke-width="2.4"/>
          <path d="M16 8v5.5a2.5 2.5 0 0 0 5 0V12a9 9 0 1 0-3.5 7.1" fill="none" stroke="#1e7f82" stroke-width="2.4" stroke-linecap="round"/>
        </svg>
        email@website.com
      </li>
    </ul>
  </section>

  <section class="card card--back">
    <div class="back-shade" role="img" aria-label="Large semi-transparent pale teal geometric shading across the left of the card"></div>
    <div class="brand"><span class="brand__dot"></span>Halvern</div>
  </section>
</body>
</html>
```